Stikers for GPS tracking company

I would like to have a sticker designed that my customers put on their vehicles and machines, to show that they have a Gps Tracking Alarm installed in their vehicle or machine.

Like stickers you use and put in your window in your home to show you have video surveillance system installed in your house.

It should be 10 cm high and 7 cm wide.

I have attached a version i have made myself, but im not satisfied with it

Target Market(s)

This is stickers that will sit on my customers assets, so the Volmira logo should be less visible and large,

Industry/Entity Type

GPS tracking and fleet management

Font styles to use
Sans Serif

Colors
0054AA
0677BA
7BADD7
CADEEF
E8F1F8

Requirements
Must have
• There should be an indication of location awareness

```html
<!DOCTYPE html>
<html lang="en">
<head>
<meta charset="utf-8">
<title>Volmira – GPS Tracking Alarm Sticker</title>
<link href="https://fonts.googleapis.com/css2?family=Roboto:wght@700;900&display=swap" rel="stylesheet">
<style>
  :root {
    --sticker-blue: #1b6bb3;
    --cream: #f3efe6;
    --brand-square: #3f9bd9;
    --brand-text: #ffffff;
  }
  html, body {
    margin: 0;
    padding: 0;
    width: 800px;
    height: 1200px;
    overflow: hidden;
    background: var(--sticker-blue);
  }
  .sticker {
    position: relative;
    width: 800px;
    height: 1200px;
    background: var(--sticker-blue);
    font-family: "Roboto", Arial, sans-serif;
  }
  .sticker-art {
    position: absolute;
    inset: 0;
  }
  .headline {
    font-weight: 900;
    fill: var(--cream);
    text-anchor: middle;
  }
  .headline--warning { font-size: 122px; }
  .headline--service { font-size: 84px; font-weight: 700; }
  .headline--alarm { font-size: 124px; font-weight: 700; }
  .brand-name {
    font-weight: 700;
    font-size: 96px;
    fill: var(--brand-text);
  }
</style>
</head>
<body>
  <main class="sticker">
    <svg class="sticker-art" width="800" height="1200" viewBox="0 0 800 1200" xmlns="http://www.w3.org/2000/svg">
      <!-- border frame -->
      <rect class="frame" x="44" y="83" width="713" height="1028" rx="60" ry="60"
            fill="none" stroke="var(--cream)" stroke-width="25"/>

      <!-- alert symbol -->
      <g class="alert-badge">
        <rect x="287" y="127" width="227" height="227" rx="24" fill="var(--cream)"/>
        <path d="M381 168 Q381 160 389 160 L411 160 Q419 160 419 168 L412 266 Q411 272 405 272 L395 272 Q389 272 388 266 Z"
              fill="var(--sticker-blue)"/>
        <circle cx="400" cy="302" r="20" fill="var(--sticker-blue)"/>
      </g>

      <!-- headline -->
      <text class="headline headline--warning" x="400" y="478">WARNING</text>
      <text class="headline headline--service" x="400" y="586">GPS TRACKING</text>
      <text class="headline headline--alarm" x="400" y="704">ALARM</text>

      <!-- location indicator -->
      <g class="location-badge">
        <circle cx="400" cy="842" r="114" fill="var(--cream)"/>
        <path d="M448 789 Q453 786 451 792 L403 899 Q399 905 397 898 L388 864 L347 852 Q340 849 346 846 Z"
              fill="var(--sticker-blue)"/>
      </g>

      <!-- brand -->
      <g class="brand">
        <rect x="159" y="986" width="81" height="81" rx="8" fill="var(--brand-square)"/>
        <text class="brand-name" x="268" y="1062">Volmira</text>
      </g>
    </svg>
  </main>
</body>
</html>
```